Auto Mechanic business card

Need a general business card for GearFixer.
Name on card should be 'Roadside Wrench'
Tel # (869) 412 3097
Address is - Palm Lane, Basseterre, St. Kitts
Whatsapp and facebook symbols should be added
On back of card should include services offered
General Repairs
Brakes
Tune Ups
Suspensions
Oil Leaks
Dent repairs
Suspensions
Car Sales
Tyre Repairs
General service
Check Engine Light
Minor Electricals

Target Market(s)

General Population, University students

Industry/Entity Type

Auto Mechanic

Contact Information for Business Card

Roadside Wrench

Requirements
Must have
• 2 Sides

```html
<!DOCTYPE html>
<html lang="en">
<head>
<meta charset="utf-8">
<title>Roadside Wrench – Business Card</title>
<link href="https://fonts.googleapis.com/css2?family=Russo+One&family=Roboto+Condensed:wght@400;700;900&display=swap" rel="stylesheet">
<style>
  :root{
    --bg:#e9e6e1;
    --card-white:#ffffff;
    --ink:#1c1c1e;
    --charcoal:#2a2a2d;
    --black:#0d0d0f;
    --red:#d9261c;
    --orange:#f28a1a;
    --light-grey:#ececec;
    --white:#ffffff;
    --chat-green:#2fb44a;
    --social-blue:#2f5ca8;
  }
  *{box-sizing:border-box;margin:0;padding:0}
  html,body{width:900px;height:1200px;overflow:hidden;background:var(--bg)}
  body{font-family:"Roboto Condensed",Arial,sans-serif;position:relative}

  .card{
    position:absolute;left:60px;width:780px;height:450px;
    border-radius:22px;overflow:hidden;
    box-shadow:0 10px 28px rgba(0,0,0,.22);
  }

  /* ---------- Front ---------- */
  .card-front{top:110px;background:var(--card-white)}
  .front-brand{position:absolute;left:0;right:0;top:70px;text-align:center}
  .brand-name{
    font-family:"Russo One",Arial,sans-serif;font-size:62px;line-height:1;
    color:var(--ink);letter-spacing:1px;
  }
  .brand-tagline{
    margin-top:10px;font-weight:700;font-size:20px;letter-spacing:2px;color:var(--red);
  }
  .phone-band{position:absolute;left:0;top:232px;width:100%;height:70px}
  .phone-band svg{position:absolute;inset:0}
  .phone-line{
    position:absolute;left:34px;top:14px;display:flex;align-items:center;gap:14px;
    color:var(--white);font-weight:700;font-size:34px;letter-spacing:1px;
  }
  .phone-icon{width:40px;height:40px;border-radius:50%;background:var(--red);display:flex;align-items:center;justify-content:center}
  .social{position:absolute;right:42px;top:318px;display:flex;gap:10px}
  .social-dot{width:38px;height:38px;border-radius:50%}
  .social-chat{background:var(--chat-green)}
  .social-page{background:var(--social-blue)}
  .address{
    position:absolute;left:34px;top:340px;font-weight:700;font-size:24px;color:var(--ink);letter-spacing:.5px;
  }
  .hours{
    position:absolute;right:0;top:388px;background:var(--charcoal);color:var(--white);
    font-weight:700;font-size:18px;padding:10px 36px 10px 26px;border-top-left-radius:16px;letter-spacing:.5px;
  }

  /* ---------- Back ---------- */
  .card-back{top:640px;background:linear-gradient(160deg,#1d1d20 0%,var(--black) 60%)}
  .back-brand{position:absolute;left:40px;top:34px;width:440px}
  .back-brand .brand-name{color:var(--white);font-size:54px;line-height:1.02}
  .back-brand .brand-tagline{color:var(--orange);font-size:19px;margin-top:10px}
  .back-mark{position:absolute;right:60px;top:36px;width:160px;height:160px;border-radius:50%;background:var(--red)}
  .services{
    position:absolute;left:40px;top:222px;width:660px;
    display:grid;grid-template-columns:1fr 1fr;column-gap:40px;row-gap:6px;list-style:none;
  }
  .services li{display:flex;align-items:center;gap:12px;color:var(--white);font-weight:700;font-size:22px;letter-spacing:.5px}
  .services li::before{content:"";width:14px;height:14px;border-radius:50%;background:var(--red);border:2px solid var(--orange);flex:none}
</style>
</head>
<body>

<section class="card card-front" aria-label="Business card front">
  <div class="front-brand">
    <div class="brand-name">ROADSIDE WRENCH</div>
    <div class="brand-tagline">SERVICE • REPAIR • MAINTENANCE</div>
  </div>

  <div class="phone-band">
    <svg viewBox="0 0 780 70" preserveAspectRatio="none" aria-hidden="true">
      <polygon points="0,0 520,0 480,70 0,70" fill="#1c1c1e"/>
      <polygon points="532,0 780,0 780,18 522,18" fill="#d9261c"/>
      <polygon points="515,28 780,28 780,44 506,44" fill="#f28a1a"/>
      <polygon points="500,54 780,54 780,70 492,70" fill="#ececec"/>
    </svg>
    <div class="phone-line">
      <span class="phone-icon">
        <svg width="22" height="22" viewBox="0 0 24 24" aria-hidden="true"><path fill="#fff" d="M6.6 10.8a15.1 15.1 0 0 0 6.6 6.6l2.2-2.2a1 1 0 0 1 1-.25 11.4 11.4 0 0 0 3.6.57 1 1 0 0 1 1 1V20a1 1 0 0 1-1 1A17 17 0 0 1 3 4a1 1 0 0 1 1-1h3.5a1 1 0 0 1 1 1c0 1.25.2 2.46.57 3.6a1 1 0 0 1-.25 1z"/></svg>
      </span>
      (869) 412 3097
    </div>
  </div>

  <div class="social">
    <span class="social-dot social-chat" role="img" aria-label="Chat app"></span>
    <span class="social-dot social-page" role="img" aria-label="Social page"></span>
  </div>

  <div class="address">PALM LANE, BASSETERRE, ST. KITTS</div>
  <div class="hours">MON - SAT : 9AM - 5PM</div>
</section>

<section class="card card-back" aria-label="Business card back">
  <div class="back-brand">
    <div class="brand-name">ROADSIDE<br>WRENCH</div>
    <div class="brand-tagline">SERVICE • REPAIR • MAINTENANCE</div>
  </div>
  <div class="back-mark" aria-hidden="true"></div>
  <ul class="services">
    <li>GENERAL REPAIRS</li><li>SUSPENSIONS</li>
    <li>BRAKES</li><li>CAR SALES</li>
    <li>TUNE UPS</li><li>TYRE REPAIRS</li>
    <li>SUSPENSIONS</li><li>GENERAL SERVICE</li>
    <li>OIL LEAKS</li><li>CHECK ENGINE LIGHT</li>
    <li>DENT REPAIRS</li><li>MINOR ELECTRICALS</li>
  </ul>
</section>

</body>
</html>
```